Plakat-Design 24h Betreuung
Zielgruppe
Wir vermitteln 24h Pflege- und Betreuungskräfte für alte und hilfbedürftige Menschen!
Zielgruppe: deren Angehörige (zwischen 50-70 Jahre alt)
Aufgabenstellung
Klare Ansage - nicht zu verspielt - geradlinig
Maße Plakat: 504 cm breit x 238 cm hoch
Das PLAKAT ist ca 10 m von der Straße entfernet und ist für Autofahrer gedacht - somit muss man alles gut lesen können und groß geschrieben sein !!!!
Folgender Text und Bilder sollte das Plakat beinhalten:
24h - Betreuung (groß links oben platziert)
Logo: SorgeHafen.at
Foto mit 10 Personen
Erfahrung seit 2010
www.sorgehafen.at

```html
<!DOCTYPE html>
<html lang="de">
<head>
<meta charset="utf-8">
<title>24h Betreuung – Plakat</title>
<link rel="stylesheet" href="https://fonts.googleapis.com/css2?family=Arimo:wght@400;700&display=swap">
<style>
  :root {
    --orange: #e8731c;
    --blue: #26478c;
    --paper: #ffffff;
    --page: #ffffff;
    --photo-light: #f1f3f7;
    --photo-mid: #c9d3e6;
  }
  * { margin: 0; padding: 0; box-sizing: border-box; }
  html, body {
    width: 1200px;
    height: 848px;
    overflow: hidden;
    background: var(--page);
    font-family: "Arimo", Arial, sans-serif;
  }
  .poster {
    position: absolute;
    left: 40px;
    top: 160px;
    width: 1120px;
    height: 528px;
    background: var(--paper);
  }
  .headline {
    position: absolute;
    left: 38px;
    top: 18px;
    font-size: 88px;
    font-weight: 700;
    line-height: 1;
    letter-spacing: -1px;
    color: var(--blue);
  }
  .headline .hours { color: var(--orange); }
  .experience {
    position: absolute;
    right: 36px;
    top: 32px;
    text-align: center;
    font-size: 39px;
    font-weight: 700;
    line-height: 1.08;
    color: var(--blue);
  }
  .experience .since { display: block; color: var(--orange); }
  .locations {
    position: absolute;
    left: 38px;
    top: 192px;
    font-size: 29px;
    font-weight: 700;
    line-height: 35px;
  }
  .locations dt { color: var(--orange); }
  .locations dd { color: var(--blue); }
  .team-photo {
    position: absolute;
    left: 348px;
    top: 118px;
    width: 530px;
    height: 392px;
    background: radial-gradient(ellipse at 50% 45%, var(--photo-mid) 0%, var(--photo-light) 70%, var(--paper) 100%);
  }
  .website {
    position: absolute;
    left: 38px;
    bottom: 30px;
    font-size: 30px;
    font-weight: 700;
    color: var(--orange);
  }
  .brand {
    position: absolute;
    right: 36px;
    bottom: 30px;
    display: flex;
    flex-direction: column;
    align-items: flex-end;
    gap: 10px;
  }
  .brand-dot {
    width: 64px;
    height: 64px;
    border-radius: 50%;
    background: var(--orange);
  }
  .brand-name {
    font-size: 28px;
    font-weight: 700;
    color: var(--blue);
  }
</style>
</head>
<body>
  <section class="poster">
    <h1 class="headline"><span class="hours">24h</span>Betreuung</h1>

    <p class="experience">Erfahrung <span class="since">seit 2010</span></p>

    <dl class="locations">
      <dt>Zentrale:</dt>
      <dd>Lindenau am See</dd>
      <dt>Zweigstelle:</dt>
      <dd>Birkenkirchen</dd>
    </dl>

    <div class="team-photo" role="img" aria-label="Gruppenfoto des Teams: zehn Betreuungskräfte in weißen Blusen und blauen Halstüchern, in der Mitte eine Frau im blauen Kostüm"></div>

    <p class="website">www.sorgehafen.at</p>

    <div class="brand">
      <span class="brand-dot"></span>
      <span class="brand-name">SorgeHafen.at</span>
    </div>
  </section>
</body>
</html>
```